Prepare a modern, professional business card for Bramford Ledger Services (BLS) Our company is in the banking, compliance and finance industry. We provide kiosks, software integration, and compliance guidelines so that banks can "bank" Marijuana Dispensaries with TrevMon, Office of Halvern Affairs and NTRB approval.

Target Market(s)

Banks

Industry/Entity Type

Business

Contact Information for Business Card

Owen R Pelley
Bramford Ledger Services
Vice President
742 Quarry Ridge Road
Suite 310
Las Vegas, NV 89135
owen@bramfordls.net
702-555-0147

Font styles to use
Sans Serif

Requirements
Nice to have
• I like the clean simple appearance of Quillon computers. Perhaps the three LETTERS of BLS can be the LOGO on the Card and the Company name could be incorporated in the contact information. Like colors of white, black and gray

```html
<!DOCTYPE html>
<html lang="en">
<head>
<meta charset="utf-8">
<title>Bramford Ledger Services – Business Card</title>
<link rel="stylesheet" href="https://fonts.googleapis.com/css2?family=Arimo:wght@400;700&family=Noto+Serif:wght@700&display=swap">
<style>
  :root {
    --page: #ffffff;
    --frame: #c8c8c8;
    --card-grey: #acacac;
    --band-grey: #cbcbcb;
    --band-light: #e6e6e6;
    --band-dark: #858585;
    --edge-white: #fdfdfd;
    --ink: #2e2e2e;
    --ink-soft: #4a4a4a;
    --mark: #5b5b5b;
    --rule-light: #e8e8e8;
    --rule-dark: #a8a8a8;
    --card-border: #9c9c9c;
  }
  * { margin: 0; padding: 0; box-sizing: border-box; }
  html, body { width: 1200px; height: 976px; overflow: hidden; background: var(--page); }
  .sheet { position: relative; width: 1200px; height: 976px; border: 1px solid var(--frame); }
  .card { position: absolute; left: 335px; width: 530px; height: 311px; overflow: hidden; font-family: "Arimo", Arial, sans-serif; color: var(--ink); }
  .card--grey { top: 133px; background: var(--card-grey); }
  .card--white { top: 532px; background: #fff; border: 1px solid var(--card-border); }
  .band { position: absolute; left: 0; right: 0; height: 70px; }
  .card--grey .band { top: 35px; background: var(--band-grey); }
  .card--white .band { top: 35px; background: var(--band-light); }
  .band__end { position: absolute; top: 0; width: 34px; height: 100%; }
  .band__end--left { left: 0; } .band__end--right { right: 0; }
  .card--grey .band__end { background: var(--edge-white); }
  .card--white .band__end { background: var(--band-dark); }
  .wordmark { position: absolute; left: 0; right: 0; top: 24px; text-align: center; font-weight: 700; font-size: 78px; line-height: 82px; letter-spacing: -2px; color: var(--mark); }
  .company { position: absolute; left: 0; right: 0; top: 120px; text-align: center; font-family: "Noto Serif", Georgia, serif; font-weight: 700; font-size: 13px; letter-spacing: 0.4px; color: var(--ink); }
  .name { position: absolute; left: 0; right: 0; top: 170px; text-align: center; font-size: 24px; color: var(--ink); }
  .title-row { position: absolute; top: 198px; left: 0; right: 0; height: 14px; }
  .title-row__rule { position: absolute; top: 7px; height: 1px; }
  .card--grey .title-row__rule { background: var(--rule-light); left: 34px; right: 34px; }
  .card--white .title-row__rule { background: var(--rule-dark); left: 124px; right: 124px; }
  .title { position: absolute; left: 50%; transform: translateX(-50%); top: -1px; padding: 0 4px; font-size: 14px; letter-spacing: 0.3px; }
  .card--grey .title { background: var(--card-grey); color: var(--ink); border-left: 1px solid var(--rule-light); border-right: 1px solid var(--rule-light); }
  .card--white .title { background: #fff; color: var(--ink-soft); border-left: 1px solid var(--rule-dark); border-right: 1px solid var(--rule-dark); }
  .address { position: absolute; left: 0; right: 0; top: 241px; text-align: center; font-size: 16px; }
  .bullet { color: #777; font-size: 11px; vertical-align: 2px; }
  .contact { position: absolute; left: 0; right: 0; top: 266px; display: flex; justify-content: center; gap: 14px; font-size: 16px; }
  .contact__item { display: flex; align-items: center; gap: 10px; }
  .icon { width: 19px; height: 19px; }
  .card--grey .icon circle { fill: #fff; } .card--grey .icon .glyph { stroke: #8a8a8a; fill: none; }
  .card--white .icon circle { fill: #8f8f8f; } .card--white .icon .glyph { stroke: #fff; fill: none; }
</style>
</head>
<body>
<div class="sheet">

  <section class="card card--grey">
    <div class="band"><span class="band__end band__end--left"></span><span class="band__end band__end--right"></span></div>
    <div class="wordmark">BLS</div>
    <p class="company">BRAMFORD LEDGER SERVICES</p>
    <p class="name">Owen R. Pelley</p>
    <div class="title-row"><span class="title-row__rule"></span><span class="title">VICE PRESIDENT</span></div>
    <p class="address"><span class="bullet">•</span> 742 Quarry Ridge Road Suite 310 Las Vegas, NV 89135 <span class="bullet">•</span></p>
    <div class="contact">
      <span class="contact__item"><svg class="icon" viewBox="0 0 20 20"><circle cx="10" cy="10" r="10"/><circle class="glyph" cx="10" cy="10" r="2.6" stroke-width="1.5"/><path class="glyph" d="M12.6 8v3.2c0 1.4 2.3 1.4 2.3-1.2A4.9 4.9 0 1 0 12 14.3" stroke-width="1.5"/></svg>owen@bramfordls.net</span>
      <span class="contact__item"><svg class="icon" viewBox="0 0 20 20"><circle cx="10" cy="10" r="10"/><circle class="glyph" cx="10" cy="10" r="6" stroke-width="1.3"/><path class="glyph" d="M7.6 6.8c-.8 1.7.9 5 3.6 6.2l1.2-1.3-1.5-1-0.8.6c-.8-.5-1.6-1.4-1.9-2.2l.7-.7-.9-1.6z" stroke-width="1.1"/></svg>702-555-0147</span>
    </div>
  </section>

  <section class="card card--white">
    <div class="band"><span class="band__end band__end--left"></span><span class="band__end band__end--right"></span></div>
    <div class="wordmark">BLS</div>
    <p class="company">BRAMFORD LEDGER SERVICES</p>
    <p class="name">Owen R. Pelley</p>
    <div class="title-row"><span class="title-row__rule"></span><span class="title">VICE PRESIDENT</span></div>
    <p class="address">• 742 Quarry Ridge Road Suite 310 Las Vegas, NV 89135 •</p>
    <div class="contact">
      <span class="contact__item"><svg class="icon" viewBox="0 0 20 20"><circle cx="10" cy="10" r="10"/><circle class="glyph" cx="10" cy="10" r="2.6" stroke-width="1.5"/><path class="glyph" d="M12.6 8v3.2c0 1.4 2.3 1.4 2.3-1.2A4.9 4.9 0 1 0 12 14.3" stroke-width="1.5"/></svg>owen@bramfordls.net</span>
      <span class="contact__item"><svg class="icon" viewBox="0 0 20 20"><circle cx="10" cy="10" r="10"/><circle class="glyph" cx="10" cy="10" r="6" stroke-width="1.3"/><path class="glyph" d="M7.6 6.8c-.8 1.7.9 5 3.6 6.2l1.2-1.3-1.5-1-0.8.6c-.8-.5-1.6-1.4-1.9-2.2l.7-.7-.9-1.6z" stroke-width="1.1"/></svg>702-555-0147</span>
    </div>
  </section>

</div>
</body>
</html>
```